Business card for Full Stable Care Vandorpe

I would like to have me designed an professional business card with my existing logo for my company called : full stable care vandorpe gcv.
I prefer a two sided business card with on the back side only the horses head and the website : fscvandorpe-example.eu
Only one colour shouldbe all right.
The logo must appear in a nic professional way on the business card.

Other suggestion are welcome.

All copy wrights must be released by the designer after we have selected a final design.

Target Market(s)

Equestrian businesses

Industry/Entity Type

Business

Contact Information for Business Card

Laurent Vandorpe
Title: zaakvoerder
Full Stable Care Vandorpe GCV
Molkenweg 47
B - 2820 Bonheiden
België
Phone: + 32 491 68 27 04
Mail: laurent@fscvandorpe-example.eu

Font styles to use
Serif

Requirements
Must have
• My own logo
• See attached files
• Website: fscvandorpe-example.eu

```html
<!DOCTYPE html>
<html lang="nl">
<head>
<meta charset="utf-8">
<title>Full Stable Care Vandorpe – Business Card</title>
<link rel="stylesheet" href="https://fonts.googleapis.com/css2?family=EB+Garamond:wght@400;600;700&display=swap">
<style>
  :root {
    --backdrop: #1b1b1b;
    --card-light: #f7f7f7;
    --card-light-edge: #dcdcdc;
    --card-dark: #252525;
    --card-dark-edge: #1e1e1e;
    --ink: #2e2e2e;
    --ink-soft: #555555;
    --band: #232323;
    --band-text: #d6d6d6;
    --logo-light: #d9d9d9;
    --horse-tone: #3c3c3c;
    --horse-tone-deep: #323232;
  }
  * { box-sizing: border-box; margin: 0; padding: 0; }
  html, body {
    width: 1200px; height: 873px; overflow: hidden;
    background: var(--backdrop);
    font-family: "EB Garamond", Georgia, serif;
  }
  .canvas { position: relative; width: 1200px; height: 873px; }

  .card {
    position: absolute;
    width: 560px; height: 340px;
    border-radius: 16px;
    overflow: hidden;
    box-shadow: 0 18px 40px rgba(0,0,0,.55);
  }

  /* Front */
  .card--front {
    left: 50px; top: 70px;
    background: radial-gradient(ellipse at 55% 40%, #ffffff 0%, var(--card-light) 55%, var(--card-light-edge) 100%);
    color: var(--ink);
  }
  .front__logo {
    position: absolute; top: 58px; left: 0; right: 0;
    display: flex; justify-content: center; align-items: center; gap: 10px;
  }
  .logo-mark {
    width: 14px; height: 14px; border-radius: 50%;
    background: var(--ink); flex: none;
  }
  .logo-name {
    font-weight: 700; font-size: 27px; letter-spacing: .5px; color: var(--ink);
    white-space: nowrap;
  }
  .front__person {
    position: absolute; left: 70px; top: 158px; width: 190px; text-align: right;
  }
  .person__name { font-weight: 700; font-size: 22px; color: var(--ink); white-space: nowrap; }
  .person__title { font-size: 16px; color: var(--ink-soft); margin-top: 2px; }
  .front__divider {
    position: absolute; left: 282px; top: 136px; width: 2px; height: 100px;
    background: linear-gradient(to bottom, transparent, #8a8a8a 30%, #8a8a8a 70%, transparent);
  }
  .front__contact {
    position: absolute; left: 304px; top: 140px; list-style: none;
    font-size: 15px; color: var(--ink-soft);
  }
  .front__contact li { display: flex; align-items: center; gap: 10px; height: 30px; white-space: nowrap; }
  .front__contact svg { width: 14px; height: 14px; fill: var(--ink); flex: none; }
  .front__band {
    position: absolute; left: 0; right: 0; bottom: 0; height: 40px;
    background: var(--band); color: var(--band-text);
    display: flex; align-items: center; justify-content: center;
    font-weight: 600; font-size: 15px; letter-spacing: .5px;
  }

  /* Back */
  .card--back {
    left: 590px; top: 463px;
    background: linear-gradient(160deg, var(--card-dark) 0%, var(--card-dark-edge) 100%);
  }
  .back__decoration {
    position: absolute; left: 20px; top: 30px; width: 250px; height: 300px;
    border-radius: 46% 40% 30% 50%;
    background: radial-gradient(ellipse at 50% 40%, var(--horse-tone) 0%, var(--horse-tone-deep) 70%, transparent 100%);
  }
  .back__logo {
    position: absolute; right: 34px; top: 190px;
    display: flex; align-items: center; gap: 10px;
  }
  .back__logo .logo-mark { background: var(--logo-light); }
  .back__logo .logo-name { color: var(--logo-light); font-size: 29px; }
</style>
</head>
<body>
<main class="canvas">

  <section class="card card--front" aria-label="Card front">
    <div class="front__logo">
      <span class="logo-mark"></span>
      <span class="logo-name">Full Stable Care Vandorpe</span>
    </div>

    <div class="front__person">
      <p class="person__name">Laurent Vandorpe</p>
      <p class="person__title">Zaakvoerder</p>
    </div>

    <div class="front__divider"></div>

    <ul class="front__contact">
      <li>
        <svg viewBox="0 0 24 24" aria-hidden="true"><path d="M6.6 10.8a15.1 15.1 0 0 0 6.6 6.6l2.2-2.2a1 1 0 0 1 1-.25 11.4 11.4 0 0 0 3.6.57 1 1 0 0 1 1 1V20a1 1 0 0 1-1 1A17 17 0 0 1 3 4a1 1 0 0 1 1-1h3.5a1 1 0 0 1 1 1c0 1.25.2 2.45.57 3.57a1 1 0 0 1-.25 1z"/></svg>
        + 32 491 68 27 04
      </li>
      <li>
        <svg viewBox="0 0 24 24" aria-hidden="true"><path d="M2 5h20v2l-10 7L2 7z M2 9l10 7 10-7v10H2z"/></svg>
        laurent@fscvandorpe-example.eu
      </li>
      <li>
        <svg viewBox="0 0 24 24" aria-hidden="true"><path d="M10.6 13.4a1 1 0 0 1 0-1.4l3.5-3.5a3 3 0 1 1 4.2 4.2l-2.1 2.1-1.4-1.4 2.1-2.1a1 1 0 1 0-1.4-1.4L12 13.4a1 1 0 0 1-1.4 0zM13.4 10.6a1 1 0 0 1 0 1.4l-3.5 3.5a3 3 0 1 1-4.2-4.2l2.1-2.1 1.4 1.4-2.1 2.1a1 1 0 1 0 1.4 1.4L12 10.6a1 1 0 0 1 1.4 0z"/></svg>
        www.fscvandorpe-example.eu
      </li>
    </ul>

    <div class="front__band">Molkenweg 47 B-2999 Veldhoek, België</div>
  </section>

  <section class="card card--back" aria-label="Card back">
    <div class="back__decoration" role="img" aria-label="Large faint horse head emblem in dark grey"></div>
    <div class="back__logo">
      <span class="logo-mark"></span>
      <span class="logo-name">Full Stable Care Vandorpe</span>
    </div>
  </section>

</main>
</body>
</html>
```